Locksmith Business Cards

My father-in-law is in need of new business cards for his locksmith business and I need to impress him. Kindly help me out!

You can see the previous business card attached. It is a family run business in North Wales.

No individual names on the cards.

Key Things to Feature:
- The words "Prompt", "Local", "Reliable" (as you can see under the logo on the website)
- 24h Emergency Service
- Covering All of North Wales, the Wirral and Chester
- The color blue
- A key or a lock would be interesting (similar to the ones that come up when you google locksmith business card)

Optional (only if design includes bullet points, like the example below):
https://imgvaultcdnx.net/design_img/318264/57190/57190_2749031_318264_image.jpg
- Residential / Commercial / Automotive
- Alarms & Cameras
- Key Cutting & Safes

https://www.bryncoed-locksmiths-demo.co.uk/

Locksmith

01632 960 418
07700 900 362
bryncoedlocksmiths@mailvalex.com
Bryncoed Locksmiths, Hafod Barn, 4 Pennant Rd., Penrhynfor LL39 7QZ
www.bryncoed-locksmiths-demo.co.uk

• - The words "Prompt", "Local", "Reliable" (as you can see under the logo on the website)
• - 24h Emergency Service
• - Covering All of North Wales, the Wirral and Chester
• - A key or a lock would be interesting (similar to the ones that come up when you google locksmith business card)

```html
<!DOCTYPE html>
<html lang="en">
<head>
<meta charset="utf-8">
<title>Bryncoed Locksmiths – Business Cards</title>
<link rel="stylesheet" href="https://fonts.googleapis.com/css2?family=Oswald:wght@500&family=Open+Sans:ital,wght@0,400;0,600;1,600&display=swap">
<style>
  :root {
    --navy: #2b2d7c;
    --blue: #46529a;
    --blue-soft: #5b66b3;
    --grey-text: #444444;
    --light-text: #e6e6e6;
    --paper: #ffffff;
    --night: #050505;
    --stage: #e9eaee;
  }
  * { box-sizing: border-box; margin: 0; padding: 0; }
  html, body { width: 1200px; height: 900px; overflow: hidden; }
  body {
    background: var(--stage);
    font-family: "Open Sans", Arial, sans-serif;
    position: relative;
  }
  .card {
    position: absolute;
    left: 250px;
    width: 700px;
    height: 400px;
    border-radius: 28px;
    overflow: hidden;
    box-shadow: 0 6px 18px rgba(0,0,0,0.12);
  }

  /* Shared company name: one font, one weight, one colour */
  .brand { position: absolute; display: flex; align-items: center; gap: 12px; }
  .brand-mark { width: 28px; height: 28px; border-radius: 50%; flex: none; }
  .brand-name {
    font-family: "Open Sans", Arial, sans-serif;
    font-weight: 600;
    font-size: 28px;
    line-height: 1.1;
    white-space: nowrap;
  }

  /* Front */
  .card-front { top: 30px; background: var(--paper); }
  .person { position: absolute; left: 52px; top: 50px; }
  .person-name {
    font-family: "Oswald", Arial, sans-serif;
    font-weight: 500; font-size: 38px; letter-spacing: 0.5px;
    color: var(--navy); line-height: 1;
  }
  .person-title {
    font-family: "Oswald", Arial, sans-serif; font-weight: 500;
    font-size: 15px; letter-spacing: 0.5px;
    color: var(--blue-soft); margin-top: 6px;
  }
  .card-front .brand { right: 52px; top: 70px; }
  .card-front .brand-mark { background: var(--navy); }
  .card-front .brand-name { color: var(--navy); }
  .contacts { position: absolute; left: 52px; top: 170px; list-style: none; }
  .contacts li {
    display: flex; align-items: center; gap: 10px;
    font-size: 16px; color: var(--grey-text); line-height: 28px;
  }
  .contacts svg { width: 14px; height: 14px; fill: var(--navy); flex: none; }
  .divider {
    position: absolute; left: 52px; right: 52px; top: 265px;
    height: 1.5px; background: var(--blue);
  }
  .address {
    position: absolute; right: 52px; top: 280px; text-align: right;
    font-style: normal; font-size: 16px; line-height: 24px; color: var(--grey-text);
  }
  .web-band {
    position: absolute; left: 0; right: 0; bottom: 0; height: 40px;
    background: var(--navy); color: var(--paper);
    font-size: 16px; display: flex; align-items: center; padding-left: 52px;
  }

  /* Back */
  .card-back { top: 470px; background: var(--night); }
  .card-back .brand { left: 52px; top: 48px; }
  .card-back .brand-mark { background: var(--blue-soft); }
  .card-back .brand-name { color: var(--blue-soft); }
  .tagline {
    position: absolute; left: 92px; top: 96px;
    font-style: italic; font-weight: 600; font-size: 16px; color: var(--blue-soft);
  }
  .services { position: absolute; left: 52px; top: 150px; list-style: none; }
  .services li {
    font-size: 16px; color: var(--light-text); line-height: 26px;
    padding-left: 14px; position: relative;
  }
  .services li::before {
    content: ""; position: absolute; left: 0; top: 11px;
    width: 5px; height: 5px; border-radius: 50%; background: var(--blue-soft);
  }
  .back-band { position: absolute; left: 0; bottom: 0; width: 700px; height: 42px; }
  .back-band polygon { fill: var(--blue); }
  .back-web {
    position: absolute; left: 52px; bottom: 10px;
    font-size: 16px; color: #eeeeee;
  }
</style>
</head>
<body>

<section class="card card-front" aria-label="Business card front">
  <div class="person">
    <p class="person-name">YOUR NAME</p>
    <p class="person-title">JOB TITLE</p>
  </div>

  <div class="brand">
    <span class="brand-mark"></span>
    <p class="brand-name">Bryncoed Locksmiths</p>
  </div>

  <ul class="contacts">
    <li><svg viewBox="0 0 24 24"><path d="M6.6 10.8a15.1 15.1 0 0 0 6.6 6.6l2.2-2.2c.3-.3.7-.4 1-.2 1.1.4 2.3.6 3.6.6.6 0 1 .4 1 1V20c0 .6-.4 1-1 1A17 17 0 0 1 3 4c0-.6.4-1 1-1h3.5c.6 0 1 .4 1 1 0 1.3.2 2.5.6 3.6.1.3 0 .7-.2 1z"/></svg>01632 960 418</li>
    <li><svg viewBox="0 0 24 24"><path d="M7 1h10a2 2 0 0 1 2 2v18a2 2 0 0 1-2 2H7a2 2 0 0 1-2-2V3a2 2 0 0 1 2-2zm0 3v14h10V4zm5 15.5a1.2 1.2 0 1 0 0 2.4 1.2 1.2 0 0 0 0-2.4z"/></svg>07700 900 362</li>
    <li><svg viewBox="0 0 24 24"><path d="M2 5h20v14H2zm2 2v.5l8 5 8-5V7zm0 2.8V17h16V9.8l-8 5z"/></svg>bryncoedlocksmiths@mailvalex.com</li>
  </ul>

  <div class="divider"></div>

  <address class="address">
    Bryncoed Locksmiths,<br>
    Hafod Barn, 4 Pennant Rd.,<br>
    Penrhynfor LL39 7QZ
  </address>

  <div class="web-band">www.bryncoed-locksmiths-demo.co.uk</div>
</section>

<section class="card card-back" aria-label="Business card back">
  <div class="brand">
    <span class="brand-mark"></span>
    <p class="brand-name">Bryncoed Locksmiths</p>
  </div>
  <p class="tagline">Prompt. Local. Reliable.</p>

  <ul class="services">
    <li>Residential / Commercial / Automotive</li>
    <li>Alarms &amp; Cameras</li>
    <li>Key Cutting &amp; Safes</li>
    <li>24h Emergency Service</li>
    <li>Covering All of North Wales, the Wirral and Chester</li>
  </ul>

  <svg class="back-band" viewBox="0 0 700 42" aria-hidden="true">
    <polygon points="0,6 430,6 410,42 0,42"/>
    <polygon points="430,26 700,26 700,34 425,34"/>
  </svg>
  <p class="back-web">www.bryncoed-locksmiths-demo.co.uk</p>
</section>

</body>
</html>
```